Graphic design of book (Grand hinge layouts)

The book is currently in Microsoft Word format. It consists mostly of images and some text. I have 21 pages and it's planned to go to print. The book front and back cover will be done separately and given to the designer. The book at print shouldn't weigh more than 1 lbs. It's short and concise book. Images need to be symmetrically sorted on the page. It's supposed to look very dense so very little "white space". Graphic design should be simple with proper titles and accents. Readers should look at it and see a "cookbook" format

```html
<!DOCTYPE html>
<html lang="en">
<head>
<meta charset="utf-8">
<title>Grand hinge layouts — Introduction</title>
<link rel="stylesheet" href="https://fonts.googleapis.com/css2?family=Source+Sans+3:wght@400;600&display=swap">
<style>
  :root {
    --navy: #1f4a7f;
    --navy-deep: #1a4277;
    --orange: #f79a4a;
    --ink: #1d1d1d;
    --paper: #ffffff;
  }
  * { margin: 0; padding: 0; box-sizing: border-box; }
  html, body {
    width: 927px; height: 1200px; overflow: hidden;
    background: var(--paper);
  }
  .page {
    position: relative; width: 927px; height: 1200px; overflow: hidden;
    font-family: "Source Sans 3", Arial, sans-serif;
    color: var(--ink);
  }
  .header-band {
    position: absolute; left: 0; top: 27px; width: 848px; height: 43px;
    background: var(--navy);
  }
  .header-tab {
    position: absolute; left: 848px; top: 0; width: 79px; height: 88px;
    background: var(--navy-deep);
  }
  .chapter-title {
    position: absolute; left: 222px; top: 34px;
    font-size: 21px; font-weight: 400; letter-spacing: 5.5px;
    color: var(--paper); text-transform: uppercase; white-space: nowrap;
  }
  .intro {
    position: absolute; left: 109px; width: 720px;
    font-size: 16px; line-height: 22.5px;
  }
  .intro.justified { text-align: justify; }
  .bullet {
    position: absolute; left: 109px; font-size: 16px; line-height: 22.5px;
  }
  .bullet .dot { display: inline-block; width: 55px; }
  .footer-tab {
    position: absolute; left: 0; top: 1103px; width: 106px; height: 86px;
    background: var(--orange);
  }
  .footer-band {
    position: absolute; left: 106px; top: 1124px; width: 821px; height: 43px;
    background: var(--orange);
  }
  .copyright {
    position: absolute; left: 495px; top: 1134px;
    font-size: 16px; font-weight: 600; letter-spacing: 3.4px;
    color: var(--ink); white-space: nowrap;
  }
</style>
</head>
<body>
<div class="page">
  <div class="header-band"></div>
  <div class="header-tab"></div>
  <h1 class="chapter-title">Grand hinge layouts</h1>

  <p class="intro" style="top:113px">Failure starts before you even put the blade to the tissue.</p>
  <p class="intro" style="top:156px">Failure starts with poor planning&nbsp;&nbsp;&nbsp;&nbsp;&nbsp;&nbsp;&nbsp;like not choosing the right flap design for your<br>case.</p>
  <p class="intro" style="top:218px">Most of what we learn about soft tissue and flap design in dental schools and<br>other programs is dogma &amp; hype. Despite dentists going through major training,<br>over 50% of all surgical cases have soft tissue problems. You too may be<br>struggling right now.</p>
  <p class="intro" style="top:325px">Here’s the good news</p>
  <p class="bullet" style="top:360px"><span class="dot">•</span>You can master soft tissue skills.</p>
  <p class="bullet" style="top:395px"><span class="dot">•</span>You can learn to “see and think” like a surgeon.</p>
  <p class="intro" style="top:437px">This book teaches you the best flap designs for various procedures that I’ve used<br>for past 20 years.</p>
  <p class="intro" style="top:499px">If you are currently struggling with flap design,&nbsp;&nbsp;&nbsp;&nbsp;&nbsp;&nbsp;&nbsp;&nbsp;&nbsp;my goal is not to further confuse<br>you but rather give you clarity and confidence. I created a simple and concise<br>method to convey the steps and illustrate so you fully understand.</p>
  <p class="intro" style="top:613px;width:712px">I risk the impression of a simplistic&nbsp;&nbsp;&nbsp;&nbsp;&nbsp;&nbsp;“recipe book”. Here’s what I’m thinking&nbsp;&nbsp;&nbsp;&nbsp;&nbsp;&nbsp;&nbsp;&nbsp;&nbsp;. You<br>are intelligent and know reading a 20 page book is part of the big picture. This is<br>why I created an online course that goes right along with this book plus many<br>other resources that teach you how to master the soft tissue.</p>
  <p class="intro" style="top:736px">Enjoy this book and master&nbsp;&nbsp;&nbsp;&nbsp;&nbsp;&nbsp;flap design.</p>
  <p class="intro" style="top:772px">To your surgical success!</p>
  <p class="intro" style="top:862px">Oren.</p>

  <div class="footer-tab"></div>
  <div class="footer-band"></div>
  <p class="copyright">Copyright of Hollowmere® LLC 2018</p>
</div>
</body>
</html>
```